Dunmore Air & Co business card

I need an awesome, double-sided business card designed with our new logo. I would like the one side black with the colored logo, and the back side is all yours. I'd like to see horizontal and vertical layouts. Get creative! Thank you.

Target Market(s)

HVAC, Heating and Cooling in Phoenix, AZ

Industry/Entity Type

HVAC

Contact Information for Business Card

We need our new logo on the card. Tom Harker, (623) 417-2958, tom@brightvaleair.com, www.brightvaleair.com, ROC 581427

```html
<!DOCTYPE html>
<html lang="en">
<head>
<meta charset="utf-8">
<title>Dunmore Air &amp; Co — Business Card</title>
<link href="https://fonts.googleapis.com/css2?family=Montserrat:wght@400;500;700;800&display=swap" rel="stylesheet">
<style>
  :root {
    --page: #d9d4cc;
    --card-dark: #1e1e1e;
    --card-light: #ffffff;
    --brand-blue: #1f6db5;
    --brand-orange: #ec6a24;
    --ink: #2b2b2b;
  }
  * { margin: 0; padding: 0; box-sizing: border-box; }
  html, body { width: 900px; height: 1200px; overflow: hidden; }
  body {
    background: var(--page);
    font-family: "Montserrat", Arial, sans-serif;
    position: relative;
  }
  .card {
    position: absolute;
    left: 78px;
    width: 744px;
    height: 442px;
    border-radius: 30px;
    overflow: hidden;
    background: var(--card-dark);
  }
  .card--front { top: 130px; }
  .card--back { top: 638px; }
  .card__shape { position: absolute; inset: 0; }

  .brand-name {
    position: absolute;
    color: var(--brand-blue);
    font-weight: 800;
    text-transform: uppercase;
    text-align: center;
    line-height: 1.1;
    letter-spacing: 1px;
  }
  .card--front .brand-name {
    left: 30px; width: 300px; top: 178px;
    font-size: 34px;
  }
  .card--back .brand-name {
    left: 0; width: 744px; top: 160px;
    font-size: 58px;
  }

  .contact {
    position: absolute;
    left: 482px;
    top: 128px;
    width: 240px;
    color: var(--ink);
  }
  .contact__name {
    color: var(--brand-blue);
    font-weight: 700;
    font-size: 26px;
    line-height: 1.1;
  }
  .contact__title { font-size: 16px; margin-top: 4px; }
  .contact__rule {
    width: 182px;
    height: 1.5px;
    background: var(--brand-orange);
    margin: 14px 0 0 2px;
  }
  .contact__licence { font-size: 16px; margin-top: 12px; }
  .contact__list { list-style: none; margin-top: 14px; }
  .contact__item {
    display: flex; align-items: center;
    font-size: 15.5px;
    height: 25px;
  }
  .contact__icon { width: 14px; height: 14px; margin-right: 14px; fill: var(--brand-orange); flex: none; }
</style>
</head>
<body>

<section class="card card--front" aria-label="Card front">
  <svg class="card__shape" viewBox="0 0 744 442" aria-hidden="true">
    <path d="M437,0 H744 V442 H440 C368,340 330,150 437,0 Z" fill="var(--card-light)"/>
    <path d="M352,195 C362,330 440,410 525,442 L448,442 C398,380 360,300 352,195 Z" fill="var(--brand-orange)"/>
  </svg>

  <div class="brand-name">Dunmore<br>Air &amp; Co</div>

  <div class="contact">
    <div class="contact__name">Tom Harker</div>
    <div class="contact__title">CEO &amp; Founder</div>
    <div class="contact__rule"></div>
    <div class="contact__licence">ROC 581427</div>
    <div class="contact__rule"></div>
    <ul class="contact__list">
      <li class="contact__item">
        <svg class="contact__icon" viewBox="0 0 16 16"><path d="M2 6c0-2 2-3 6-3s6 1 6 3v1h-3V5.5H5V7H2z M4 8h8l2 5H2z"/></svg>
        (623) 417-2958
      </li>
      <li class="contact__item">
        <svg class="contact__icon" viewBox="0 0 16 16"><path d="M1 4h14v1l-7 4-7-4z M1 6.5l7 4 7-4V13H1z"/></svg>
        tom@brightvaleair.com
      </li>
      <li class="contact__item">
        <svg class="contact__icon" viewBox="0 0 16 16"><circle cx="8" cy="8" r="7"/></svg>
        www.brightvaleair.com
      </li>
    </ul>
  </div>
</section>

<section class="card card--back" aria-label="Card back">
  <div class="brand-name">Dunmore<br>Air &amp; Co</div>
</section>

</body>
</html>
```